Dietitian needs a new business card design

I need a new business card design for my nutrition business that provides individual clinical nutrition advice for people with medical conditions. Business cards will be handed out to doctors, specialists and clients so will need to be sharp and project an image of professionalism

Target Market(s)

My clients are typically referred by doctors or specialists and the card will be used to handout to clients and their doctors.

Industry/Entity Type

Medical

Contact Information for Business Card

The business card will require the details below. These details can be found from my website https://www.kelvarrowclinic.com.au/

Font styles to use
Serif

Colors

Designer to choose colors to be used in the design.

Requirements
Must have
• 1. It needs be professional and contemporary
• 2. It needs to incorporate my logo
• 3. It needs space to write appointment times and dates
• 4. It needs to provide my phone number, fax number, email address and my web address
Nice to have
• Include the Registered Tovance Clinician Logo
• I have access to Framellow if required
• The locations I practise from
Should not have
• Pictures of food
• Spelling MIstakes

```html
<!DOCTYPE html>
<html lang="en">
<head>
<meta charset="utf-8">
<title>Harbourline Nutrition &amp; Dietetics – Business Card</title>
<link rel="stylesheet" href="https://fonts.googleapis.com/css2?family=Lato:wght@400;700&display=swap">
<style>
  :root {
    --bg: #26292c;
    --card: #ffffff;
    --blue: #0b5fb0;
    --green: #7bc043;
    --orange: #f07d1e;
    --ink: #333333;
  }
  * { margin: 0; padding: 0; box-sizing: border-box; }
  html, body { width: 1200px; height: 738px; overflow: hidden; }
  body {
    background: var(--bg);
    font-family: "Lato", Arial, sans-serif;
    color: var(--ink);
    position: relative;
  }
  .card {
    position: absolute;
    top: 219px;
    width: 540px;
    height: 300px;
    background: var(--card);
    overflow: hidden;
  }
  .card--back { left: 40px; }
  .card--front { left: 620px; }

  /* brand name block */
  .brand { display: flex; align-items: center; gap: 8px; color: var(--blue); font-weight: 700; }
  .brand__dot { width: 34px; height: 34px; border-radius: 50%; background: var(--green); flex: none; }
  .brand__name { line-height: 1.05; }
  .brand__title { display: block; font-size: 26px; }
  .brand__sub { display: block; font-size: 13px; }

  /* back card */
  .badge {
    position: absolute; left: 40px; top: 48px;
    width: 168px; height: 66px;
    background: var(--orange); border-radius: 5px;
    display: flex; align-items: center; justify-content: space-between;
    padding: 0 10px 0 12px;
  }
  .badge__text { color: #fff; font-size: 11px; line-height: 1.15; width: 80px; }
  .badge__seal { width: 48px; height: 48px; border-radius: 50%; background: #fff; }
  .card--back .brand { position: absolute; left: 300px; top: 56px; }
  .appointment__title {
    position: absolute; left: 0; right: 0; top: 160px;
    text-align: center; color: var(--blue); font-size: 15px;
  }
  .appointment__row {
    position: absolute; left: 70px; right: 40px; top: 212px;
    display: flex; align-items: flex-end; gap: 6px; font-size: 15px;
  }
  .appointment__line { flex: 1; border-bottom: 1px solid #444; height: 14px; }
  .appointment__label { margin-left: 4px; }

  /* front card */
  .card--front .brand { position: absolute; left: 32px; top: 100px; }
  .divider { position: absolute; left: 295px; top: 52px; width: 2px; height: 150px; background: var(--blue); }
  .contact { position: absolute; left: 312px; top: 34px; }
  .contact__name { color: var(--blue); font-weight: 700; font-size: 21px; letter-spacing: 0.5px; line-height: 1.2; }
  .contact__role { font-size: 13px; margin-bottom: 8px; }
  .contact__address { font-size: 11.5px; line-height: 1.35; margin-bottom: 6px; }
  .contact__list { list-style: none; font-size: 11.5px; line-height: 1.4; }
  .contact__list li { display: flex; align-items: center; gap: 7px; }
  .contact__list svg { width: 10px; height: 10px; fill: var(--blue); flex: none; }
  .contact__web { color: var(--green); }
  .swoosh { position: absolute; left: 0; top: 0; width: 540px; height: 300px; }
</style>
</head>
<body>

<section class="card card--back" aria-label="Card back">
  <div class="badge">
    <span class="badge__text">Registered Tovance Clinician</span>
    <span class="badge__seal"></span>
  </div>
  <div class="brand">
    <span class="brand__dot"></span>
    <span class="brand__name">
      <span class="brand__title">Harbourline</span>
      <span class="brand__sub">Nutrition &amp; Dietetics</span>
    </span>
  </div>
  <p class="appointment__title">Appointment</p>
  <div class="appointment__row">
    <span>Time</span><span class="appointment__line"></span>
    <span class="appointment__label">Date</span><span class="appointment__line"></span>
  </div>
</section>

<section class="card card--front" aria-label="Card front">
  <svg class="swoosh" viewBox="0 0 540 300" aria-hidden="true">
    <path d="M0,204 Q260,244 540,250 L540,300 L0,300 Z" fill="var(--blue)"/>
    <path d="M130,228 Q380,238 540,206" fill="none" stroke="var(--green)" stroke-width="5"/>
  </svg>
  <div class="brand">
    <span class="brand__dot"></span>
    <span class="brand__name">
      <span class="brand__title">Harbourline</span>
      <span class="brand__sub">Nutrition &amp; Dietetics</span>
    </span>
  </div>
  <div class="divider"></div>
  <div class="contact">
    <h1 class="contact__name">DANIEL ORWELL</h1>
    <p class="contact__role">Director</p>
    <p class="contact__address">5/118 Calder Street<br>Westbury Tasmania 7303</p>
    <ul class="contact__list">
      <li><svg viewBox="0 0 10 10"><path d="M2 0h2l1 3-1.5 1a6 6 0 0 0 2.5 2.5L7 5l3 1v2c0 1-1 2-2 2A8 8 0 0 1 0 2c0-1 1-2 2-2z"/></svg>0400 555 271</li>
      <li><svg viewBox="0 0 10 10"><rect x="2" y="0" width="6" height="3"/><rect x="0" y="4" width="10" height="5" rx="1"/></svg>+613 5550 4126</li>
      <li><svg viewBox="0 0 10 10"><path d="M0 2h10v6H0z M1 3l4 3 4-3" fill="none" stroke="var(--blue)" stroke-width="1"/></svg>daniel@kelvarrowclinic.com.au</li>
      <li><svg viewBox="0 0 10 10"><circle cx="5" cy="5" r="4.5"/></svg><span>www.<span class="contact__web">kelvarrowclinic</span>.com.au</span></li>
    </ul>
  </div>
</section>

</body>
</html>
```